Business Card and Letterhead for Copperfield Reed - (Have Logo)

Update 4: Removed company reg no from business card details as it looked a bit out of place. Updated services list.
UPDATE 3
Sorry, I got the address a little bit wrong, have updated it below. Sorry for any inconvenience caused.
UPDATE 2
Finally I have the details for the business cards and letterhead. Submissions already made do not have to be updated unless shortlisted, if all new submissions could include the details for me, Simon, that would be very much appreciated and help with the final shortlist selection. I intend to share a shortlist of the three best entries with past and existing customers for their feedback and opinions. Thank you all again for your time.
Here are the details.
Simon Latchford
Web Developer
T: 01632 418 720
E: simon@copperfieldreed.example
www.copperfieldreed.example
Professional Photography
Web Solutions & E-Commerce
Audio & HD Video Production
Marketing & Promotions
Identity and Branding
Copperfield Reed Ltd
Suite 20938, 3rd Floor
212-224 Marlowe Row
London, EC2R 8KT
Company Reg. No: 09264183
The order and the layout of the information are of course down to the design, but the company registration number should be smaller and less prominent. The formatting of the telephone and email address using a T: and an E: I am not sure about and again if it is Tel: or Email: or Icons is up to the design.
The Company No. on the letterhead should read (somewhere in small text along the bottom):
Copperfield Reed is a Ltd Company registered in England & Wales, Registration No. 09264183.
The second business card details are
Martin Oakley
Photographer
T: 01632 418 720
E: martin@copperfieldreed.example
Everything else the same of course.
Thank you again for all the submissions so far.
END OF UPDATE 2
-
UPDATE 1: Please do not alter the logo nor the logo colours. (This was a previous pixel bazaar project and I am extremely happy with it. The icon can stand alone of course, but I have had to eliminate all entries that have made it black and white, or reversed the icon.) I would like to thank everyone that has participated so far and am very grateful for all your thought and time.
End of Update 1
-
Original Brief:
I have attached the logo vector file.
Following a superb logo from a previous Pixel Bazaar project I am now looking for a business card design and (although less important) a letterhead as well.
I must admit I tried to do it myself but could only come up with the usual amateur stuff that in comparison to the quality of the logo looked awful.
About Us
Copperfield Reed Ltd will be a new company due to start in January. It is really just me (a web developer) and my friend (a photographer). We will be aiming at the usual small to medium sized businesses in the local area, selling various digital services including photographic services to the public, web hosting and development, commercial photography, modelling services (not us!), full video and film production and possibly a bit of marketing as well. (Really it is anything we can do professionally all lumped together! We met running seperate businesses which have both since closed)
We will not be competing on price. We plan to be expensive but fair. Certainly not the cheapest.
What we are looking for
Business Card
I imagine a double sided business card, which will be used for more than one person. I imagine the front to be the same for everyone and the persons details to be on the back, although this is of course only my thoughts and I am of course completely open to any ideas.
The card could also have a services list or a bit about what we do on it. It might feature the website address, our business address (mail forwarding address) or our registered company number.
Or it might have none of that, we are completely open to any ideas and have no real fixed opinions. I just want it to be really nice :-)
Letterhead (secondary importance)
We will make our decision primarily on the business card, although a mathcing letterhead would be fantastic. Something standardish in format and simple, although again, all ideas are welcomed.
I hope that is enough information but if you have any questions I will answer them as fully and as quickly as possible.
Thank you once again and I really look forward to seeing your ideas and picking a winner.
Simon L.
Small businesses AND the general public
Film Production

```html
<!DOCTYPE html>
<html lang="en">
<head>
<meta charset="utf-8">
<title>Copperfield Reed – Letterhead and Business Card</title>
<link rel="stylesheet" href="https://fonts.googleapis.com/css2?family=Arimo:wght@400;700&family=Lato:wght@400;700&display=swap">
<style>
  :root {
    --brand-red: #b8232f;
    --soft-red: #c9575d;
    --ink: #222222;
    --charcoal: #3d3d3d;
    --grey-rule: #b5b5b5;
    --blue: #2a7fc0;
    --pale-blue: #e4edf7;
    --cream: #fbf6f0;
    --ghost: #f5eeee;
    --paper: #ffffff;
  }
  * { margin: 0; padding: 0; box-sizing: border-box; }
  html, body { width: 1188px; height: 1200px; overflow: hidden; background: var(--paper); }
  body { position: relative; font-family: "Arimo", Arial, sans-serif; color: var(--ink); }

  .letterhead { position: absolute; left: 0; top: 0; width: 810px; height: 1200px; }
  .letterhead-art { position: absolute; left: 0; top: 0; }
  .brand-name {
    position: absolute; left: 15px; top: 92px;
    display: flex; align-items: center; gap: 10px;
    font-family: "Arimo", Arial, sans-serif; font-weight: 700; font-size: 40px;
    color: var(--charcoal); letter-spacing: 0.5px;
  }
  .brand-mark { width: 30px; height: 30px; background: var(--brand-red); }
  .contact {
    position: absolute; right: 15px; top: 88px; text-align: right;
    font-size: 15px; line-height: 18px; color: var(--brand-red);
  }
  .address-line {
    position: absolute; left: 95px; top: 180px;
    font-size: 15px; color: var(--ink);
  }
  .ghost-name {
    position: absolute; left: 100px; top: 552px;
    font-weight: 700; font-size: 72px; color: var(--ghost); letter-spacing: 1px;
  }
  .registration {
    position: absolute; left: 15px; width: 785px; top: 1064px; text-align: center;
    font-family: "Lato", sans-serif; font-size: 13.5px; color: var(--soft-red);
  }
  .website-band {
    position: absolute; left: 15px; width: 785px; top: 1086px; height: 23px;
    background: var(--cream); text-align: center;
    font-family: "Lato", sans-serif; font-size: 14px; line-height: 23px;
    letter-spacing: 3px; color: var(--brand-red);
  }

  .card-column { position: absolute; left: 831px; top: 0; }
  .card-column text { font-family: "Arimo", Arial, sans-serif; }
  .card-column .service { font-family: "Lato", sans-serif; font-variant: small-caps; }
</style>
</head>
<body>

<section class="letterhead" aria-label="Letterhead">
  <svg class="letterhead-art" width="810" height="1200" viewBox="0 0 810 1200">
    <defs>
      <linearGradient id="cornerGrey" x1="0" y1="0" x2="1" y2="1">
        <stop offset="0" stop-color="#5a5a5a"/>
        <stop offset="1" stop-color="#9a9a9a"/>
      </linearGradient>
    </defs>
    <path d="M405 170 L457 81 H800" fill="none" stroke="var(--charcoal)" stroke-width="1"/>
    <line x1="15" y1="170" x2="800" y2="170" stroke="var(--brand-red)" stroke-width="1.5"/>
    <line x1="15" y1="203" x2="800" y2="203" stroke="var(--grey-rule)" stroke-width="1"/>
    <path d="M15 203 H110 Q28 220 15 328 Z" fill="url(#cornerGrey)"/>
    <path d="M800 937 Q792 1045 665 1058 H800 Z" fill="var(--soft-red)"/>
    <line x1="15" y1="1059" x2="800" y2="1059" stroke="var(--soft-red)" stroke-width="1"/>
    <line x1="15" y1="1111" x2="800" y2="1111" stroke="var(--ink)" stroke-width="1.5"/>
  </svg>

  <div class="brand-name"><span class="brand-mark"></span>Copperfield Reed</div>
  <div class="contact">
    <div>Martin Oakley</div>
    <div>Photographer</div>
    <div>T: 01632 418 720</div>
    <div>E: martin@copperfieldreed.example</div>
  </div>
  <div class="address-line">Copperfield Reed Ltd, Suite 20938, 3rd Floor, 212-224 Marlowe Row, London, EC2R 8KT</div>
  <div class="ghost-name" aria-hidden="true">Copperfield Reed</div>
  <div class="registration">Copperfield Reed is a Ltd Company registered in England &amp; Wales, Registration No. 09264183.</div>
  <div class="website-band">www.copperfieldreed.example</div>
</section>

<svg class="card-column" width="314" height="1200" viewBox="537 0 203 768" preserveAspectRatio="none" aria-label="Business card, back and front">
  <!-- personal side -->
  <g class="card-personal">
    <line x1="543" y1="3" x2="730" y2="3" stroke="var(--brand-red)" stroke-width="0.8"/>
    <line x1="543" y1="6" x2="730" y2="6" stroke="var(--grey-rule)" stroke-width="0.8"/>
    <line x1="737" y1="0" x2="737" y2="345" stroke="var(--ink)" stroke-width="1"/>
    <text transform="translate(634 88) rotate(90)" font-size="17" fill="var(--ink)">Martin Oakley</text>
    <text class="service" transform="translate(622 128) rotate(90)" font-size="8.5" font-weight="700" fill="var(--blue)" letter-spacing="0.5">Photographer</text>
    <line x1="631" y1="196" x2="631" y2="258" stroke="var(--blue)" stroke-width="0.6"/>
    <text transform="translate(596 140) rotate(90)" font-size="7.5" fill="var(--blue)">T: 01632 418 720</text>
    <text transform="translate(585 106) rotate(90)" font-size="7.5" fill="var(--blue)">E: martin@copperfieldreed.example</text>
    <rect x="703" y="202" width="12" height="12" fill="var(--brand-red)"/>
    <text transform="translate(705 219) rotate(90)" font-size="12" font-weight="700" fill="var(--charcoal)">Copperfield Reed</text>
  </g>

  <!-- divider band -->
  <g class="card-divider">
    <rect x="537" y="346" width="201" height="50" fill="var(--ink)"/>
    <line x1="537" y1="351" x2="738" y2="351" stroke="var(--paper)" stroke-width="0.8"/>
    <line x1="537" y1="391" x2="738" y2="391" stroke="var(--paper)" stroke-width="0.8"/>
    <text transform="translate(656 362) rotate(90)" font-size="10" fill="var(--paper)">B</text>
    <path d="M643 366 L648 376 H638 Z" fill="var(--paper)"/>
    <text transform="translate(623 362) rotate(90)" font-size="10" fill="var(--paper)">C</text>
    <text transform="translate(607 362) rotate(90)" font-size="10" fill="var(--paper)">K</text>
  </g>

  <!-- company side -->
  <g class="card-company">
    <line x1="543" y1="403" x2="730" y2="403" stroke="var(--brand-red)" stroke-width="0.8"/>
    <line x1="543" y1="406" x2="730" y2="406" stroke="var(--grey-rule)" stroke-width="0.8"/>
    <line x1="737" y1="400" x2="737" y2="768" stroke="var(--ink)" stroke-width="1"/>
    <path d="M720 448 A31 46 0 0 0 689 494 H720 Z" fill="var(--charcoal)"/>
    <path d="M689 494 A31 46 0 0 0 720 540 V494 Z" fill="var(--brand-red)"/>
    <text class="service" transform="translate(676 430) rotate(90)" font-size="9" fill="var(--blue)">Professional Photography</text>
    <text class="service" transform="translate(654 430) rotate(90)" font-size="9" fill="var(--blue)">Web Solutions &amp; E-Commerce</text>
    <text class="service" transform="translate(632 430) rotate(90)" font-size="9" fill="var(--blue)">Audio &amp; HD Video Production</text>
    <text class="service" transform="translate(610 430) rotate(90)" font-size="9" fill="var(--blue)">Marketing &amp; Promotions</text>
    <text class="service" transform="translate(589 430) rotate(90)" font-size="9" fill="var(--blue)">Identity and Branding</text>
    <path d="M537 570 Q640 630 655 768 H537 Z" fill="var(--pale-blue)"/>
    <text transform="translate(574 645) rotate(90)" font-size="8" fill="var(--ink)">Copperfield Reed Ltd</text>
    <text transform="translate(563 638) rotate(90)" font-size="8" fill="var(--ink)">Suite 20938, 3rd Floor</text>
    <text transform="translate(552 632) rotate(90)" font-size="8" fill="var(--ink)">212-224 Marlowe Row</text>
    <text transform="translate(541 650) rotate(90)" font-size="8" fill="var(--ink)">London, EC2R 8KT</text>
    <rect x="703" y="606" width="12" height="12" fill="var(--brand-red)"/>
    <text transform="translate(705 623) rotate(90)" font-size="12" font-weight="700" fill="var(--charcoal)">Copperfield Reed</text>
    <rect x="690" y="750" width="48" height="18" fill="var(--ink)"/>
  </g>
</svg>

</body>
</html>
```